The First Annual Tamsworth Legacy Supper

Something similar to the attached but an attention grabber. It needs to attract people with money to spend!

```html
<!DOCTYPE html>
<html lang="en">
<head>
<meta charset="utf-8">
<title>The First Annual Tamsworth Legacy Supper</title>
<link rel="stylesheet" href="https://fonts.googleapis.com/css2?family=Barlow+Condensed:wght@500;600&family=Fira+Sans:wght@300;400;500;700;800&display=swap">
<style>
  :root {
    --page-bg: #5a5a5a;
    --paper: #ffffff;
    --brand-blue: #6a96d2;
    --brand-blue-text: #4f83cc;
    --navy: #0e3a80;
    --ink: #1f1f1f;
    --sky-top: #8fb4e0;
    --sky-mid: #d7e4f2;
    --wall: #e9edf0;
    --grass: #6f7a3a;
  }
  * { box-sizing: border-box; margin: 0; padding: 0; }
  html, body { width: 1200px; height: 1200px; overflow: hidden; background: var(--page-bg); }
  body { font-family: "Fira Sans", sans-serif; color: var(--ink); }

  .flyer {
    position: absolute; left: 160px; top: 30px;
    width: 880px; height: 1140px; background: var(--paper); overflow: hidden;
  }

  .hero-photo {
    position: absolute; left: 0; top: 0; width: 880px; height: 655px;
    background: linear-gradient(180deg, var(--sky-top) 0%, var(--sky-mid) 42%, #f2f5f8 58%, var(--wall) 70%, #c9ccc6 82%, var(--grass) 88%, #5e6631 100%);
  }

  .title-panel {
    position: absolute; left: 37px; top: 0; width: 452px; height: 365px;
    background: var(--brand-blue); color: #fff; padding: 32px 0 0 27px;
  }
  .title-panel .presenter { font-size: 23px; font-weight: 500; line-height: 34px; letter-spacing: 0.1px; }
  .title-panel .presents { font-size: 23px; font-weight: 300; line-height: 36px; margin-bottom: 8px; }
  .title-panel h1 { font-size: 41px; font-weight: 800; line-height: 51px; text-transform: uppercase; letter-spacing: 0.3px; }

  .event-time {
    position: absolute; right: 38px; top: 26px; text-align: right;
    font-family: "Barlow Condensed", sans-serif; color: var(--ink);
  }
  .event-time .date { font-size: 68px; font-weight: 600; color: var(--navy); line-height: 68px; letter-spacing: -0.5px; }
  .event-time .start { font-size: 42px; font-weight: 500; line-height: 46px; }
  .event-time .cocktail { font-size: 38px; font-weight: 500; line-height: 46px; }

  .details { position: absolute; left: 37px; top: 676px; width: 384px; }
  .details h2 { font-size: 24px; font-weight: 700; color: var(--brand-blue-text); line-height: 31px; margin-bottom: 10px; }
  .details p { font-size: 15.5px; font-weight: 300; line-height: 21px; text-align: justify; margin-bottom: 21px; }
  .details .follow { font-size: 18px; font-weight: 500; color: var(--brand-blue-text); line-height: 24px; margin-top: 28px; }

  .ticket-box {
    position: absolute; left: 460px; top: 655px; width: 385px; height: 193px;
    background: var(--brand-blue); color: #fff; border-radius: 0 0 8px 8px;
    padding: 22px 25px 0 25px; font-size: 16.5px; font-weight: 500; line-height: 22px;
    text-transform: uppercase; text-align: justify;
  }
  .ticket-box p + p { margin-top: 19px; }

  .outlets { position: absolute; left: 460px; top: 870px; width: 385px; }
  .outlets h3 { font-size: 15.5px; font-weight: 700; color: var(--brand-blue-text); text-transform: uppercase; margin-bottom: 6px; }
  .outlet-list { list-style: none; border-left: 1.5px dotted var(--brand-blue); margin-left: 4px; padding-left: 13px; }
  .outlet-list li { position: relative; margin-bottom: 10px; }
  .outlet-list li::before { content: ""; position: absolute; left: -17px; top: 7px; width: 6px; height: 6px; border-radius: 50%; background: var(--brand-blue); }
  .outlet-list .name { font-size: 16px; font-weight: 500; line-height: 21px; }
  .outlet-list .addr { font-size: 15.5px; font-weight: 300; line-height: 21px; }
  .outlets .alt { margin-top: 12px; }
  .contact { display: flex; align-items: center; gap: 6px; font-size: 13px; font-weight: 700; line-height: 24px; text-transform: uppercase; }
  .contact .phone { font-weight: 500; }
  .contact svg { width: 15px; height: 15px; }

  .footer-band { position: absolute; left: 0; bottom: 0; width: 880px; height: 11px; background: var(--brand-blue); }
</style>
</head>
<body>
  <main class="flyer">
    <div class="hero-photo" role="img" aria-label="Photo of the long white community center building with a blue metal roof under a cloudy sky, lawn in front"></div>

    <header class="title-panel">
      <p class="presenter">THE TAMSWORTH COMMUNITY CENTER</p>
      <p class="presents">PRESENTS</p>
      <h1>The First Annual<br>Tamsworth Legacy<br>Supper</h1>
    </header>

    <div class="event-time">
      <p class="date">April 23, 2022</p>
      <p class="start">starting at 5:00 pm</p>
      <p class="cocktail">with cocktail hour</p>
    </div>

    <section class="details">
      <h2>Live auction, silent auction, raffle and a cash bar!</h2>
      <p>Come on out to the Tamsworth Community Center for a delicious prime rib dinner, drinks, entertainment and more! There will be plenty of amazing auction items for everyone to choose from.</p>
      <p>All proceeds will go to the Tamsworth Community Center. We will share some history of the school and each year we will highlight a local family. This year will be the Harwell family who have been here for ....years!!</p>
      <p>High Side Barn, dirt bike, custom knives, a pack trip and so much more!</p>
      <p class="follow">Follow the Tamsworth Community Center's Townboard page to see all the auction items available!</p>
    </section>

    <section class="ticket-box">
      <p>Tickets for the event are $50 each or $90 for a couple</p>
      <p>Tickets for the 10x12 high side barn $25 each or 5 for $100. Donated by: Ridgeline Shed Co. of Cedarview, value $6500</p>
    </section>

    <section class="outlets">
      <h3>Get your tickets from:</h3>
      <ul class="outlet-list">
        <li><p class="name">Ridgeline Shed Co. in Cedarview</p><p class="addr">42 Harlow Rd, Cedarview</p></li>
        <li><p class="name">Summit Peak Realty</p><p class="addr">219 E Aspen St, Cedarview</p></li>
        <li><p class="name">Tamsworth Mercantile</p><p class="addr">6120 State Route 48, Tamsworth</p></li>
      </ul>
      <h3 class="alt">Or get them from</h3>
      <p class="contact">Dana Merrick
        <svg viewBox="0 0 16 16" aria-hidden="true"><circle cx="8" cy="8" r="7" fill="none" stroke="#4f83cc" stroke-width="1.2"/><path d="M5.3 4.6c.4-.3.9-.2 1.1.2l.6 1.2c.2.3.1.7-.2.9l-.5.4c.4.9 1.1 1.6 2 2l.4-.5c.2-.3.6-.4.9-.2l1.2.6c.4.2.5.7.2 1.1l-.5.6c-.4.4-1 .5-1.5.3-1.9-.8-3.4-2.3-4.2-4.2-.2-.5-.1-1.1.3-1.5z" fill="#4f83cc"/></svg>
        <span class="phone">(555)210-0148</span></p>
      <p class="contact">Jolene Pratt
        <svg viewBox="0 0 16 16" aria-hidden="true"><circle cx="8" cy="8" r="7" fill="none" stroke="#4f83cc" stroke-width="1.2"/><path d="M5.3 4.6c.4-.3.9-.2 1.1.2l.6 1.2c.2.3.1.7-.2.9l-.5.4c.4.9 1.1 1.6 2 2l.4-.5c.2-.3.6-.4.9-.2l1.2.6c.4.2.5.7.2 1.1l-.5.6c-.4.4-1 .5-1.5.3-1.9-.8-3.4-2.3-4.2-4.2-.2-.5-.1-1.1.3-1.5z" fill="#4f83cc"/></svg>
        <span class="phone">(555)384-2291</span></p>
    </section>

    <div class="footer-band"></div>
  </main>
</body>
</html>
```